MARLSTONE BUILDWORKS B-Card

I currently have a b-card design but will be removing the image (tree) from the logo and have text only.
I want the card to be classy and strong within the building and construction industry.
I will be using Spot UV on the cards as per the attached examples. I will also send through some sketched ideas that I have in mind.
The color blue is similar to the image (No. 6) attached images

Target Market(s)

middle to maturre aged.
Home Owners / Renovators and Builders

Industry/Entity Type

Construction

Contact Information for Business Card

MARLSTONE BUILDWORKS
Name: Gideon Pellow
Title: Project Manager
Mobile: 0472 315 084
Office: (08) 9571 2046
Address: 17C Quenby Parade, Malaga WA 6090
Email: info@marlstonehouses.example.au
PO Box: 3817 Malaga WA 6944

Colors
0592cd
33a6d7
85cae6
1b1b1b

Requirements
Must have
• 1. It must have spot UV on the front of card, maybe back of card too
• 2. I really like the blue on image 6. (or at least a really cool electric blue against the charcoal grey background)
• 3. The font must be slimline and modern. Easy to read
• 4. There must be no black used on the card... Only greys and dark charcoal greys
• 5. Use only the text from the logo "Marlstone Buildworks" Not the image of the tree. I am wanting the b-cards to be more masculine.
Nice to have
• 1. I like the design concept on image 6. but happy to see what else you can do with the Spot UV
• 2. Unless you have a really cool idea of the image of the tree (from previous logo) Spot UV somewhere in the design concept thats original and different then I am keen to see what you come up with
• 3. Try changing the color of the logo eg. full white or Blue and white
• 4. Another option is to have the Marlstone Logo on the front of card with the spot UV in the background of text which we specialise in eg, Roofing, Ceiling, Insulation, Gutter Guards, Electrical, Insurance etc and we can add or reduce items as required. Similar to image 12.
Should not have
• Do not include the image of the tree from previous logo. unless you have a really cool idea of Spot UV somewhere in the design concept thats original and different.

```html
<!DOCTYPE html>
<html lang="en">
<head>
<meta charset="utf-8">
<title>Marlstone Buildworks – Business Card</title>
<link rel="stylesheet" href="https://fonts.googleapis.com/css2?family=Open+Sans:wght@400;600;700&display=swap">
<style>
  :root {
    --stage: #5a4233;
    --electric-blue: #2ea9e1;
    --logo-blue: #33a6d7;
    --charcoal: #232323;
    --charcoal-light: #2e2e2e;
    --white: #ffffff;
    --card-shadow: 0 6px 16px rgba(0,0,0,0.35);
  }
  * { margin: 0; padding: 0; box-sizing: border-box; }
  html, body {
    width: 1200px;
    height: 1000px;
    overflow: hidden;
    background: var(--stage);
    font-family: "Open Sans", Arial, sans-serif;
  }
  .canvas {
    position: relative;
    width: 1200px;
    height: 1000px;
  }
  .card {
    position: absolute;
    left: 265px;
    width: 666px;
    height: 397px;
    box-shadow: var(--card-shadow);
    overflow: hidden;
  }
  /* Front */
  .card--front {
    top: 73px;
    background: var(--electric-blue);
    color: var(--white);
  }
  .card--front .wordmark {
    position: absolute;
    right: 32px;
    top: 66px;
    text-align: right;
    font-weight: 600;
    font-size: 25px;
    line-height: 32px;
    letter-spacing: 3px;
    color: var(--white);
  }
  .contact {
    position: absolute;
    left: 33px;
    top: 175px;
  }
  .contact__name {
    font-weight: 700;
    font-size: 19px;
    line-height: 24px;
  }
  .contact__title {
    font-size: 16px;
    line-height: 20px;
  }
  .contact__lines {
    list-style: none;
    margin-top: 18px;
    font-size: 16px;
    line-height: 23px;
  }
  .contact__lines li {
    display: flex;
    align-items: center;
    gap: 7px;
  }
  .contact__lines svg {
    width: 16px;
    height: 16px;
    fill: var(--white);
    flex: none;
  }
  .contact__post {
    margin-top: 7px;
    font-size: 16px;
    line-height: 26px;
  }
  /* Back */
  .card--back {
    top: 532px;
    background: var(--charcoal);
  }
  .spot-uv-tree {
    position: absolute;
    left: 10px;
    top: 10px;
    width: 646px;
    height: 387px;
    border-radius: 48% 48% 6px 6px / 40% 40% 6px 6px;
    background: radial-gradient(ellipse at 50% 45%, #3a3a3a 0%, #2c2c2c 55%, var(--charcoal) 100%);
  }
  .card--back .wordmark {
    position: absolute;
    left: 0;
    right: 0;
    top: 160px;
    text-align: center;
    font-weight: 600;
    font-size: 30px;
    line-height: 40px;
    letter-spacing: 5px;
    color: var(--logo-blue);
  }
</style>
</head>
<body>
<main class="canvas">
  <section class="card card--front" aria-label="Business card front">
    <div class="wordmark">MARLSTONE<br>BUILDWORKS</div>
    <div class="contact">
      <p class="contact__name">GIDEON PELLOW</p>
      <p class="contact__title">Project Manager</p>
      <ul class="contact__lines">
        <li>
          <svg viewBox="0 0 16 16" aria-hidden="true"><path d="M4.5 1h7a1 1 0 0 1 1 1v12a1 1 0 0 1-1 1h-7a1 1 0 0 1-1-1V2a1 1 0 0 1 1-1zm.5 2v9h6V3zm3 10a.7.7 0 1 0 0 1.4A.7.7 0 0 0 8 13z"/></svg>
          0472 315 084
        </li>
        <li>
          <svg viewBox="0 0 16 16" aria-hidden="true"><path d="M1 6c0-2 3-3.5 7-3.5S15 4 15 6v1.2h-3.2V5.6H4.2v1.6H1zm3.4 1.2h7.2L14 13H2zM8 8.6a2 2 0 1 0 0 4 2 2 0 0 0 0-4z"/></svg>
          (08) 9571 2046
        </li>
        <li>
          <svg viewBox="0 0 16 16" aria-hidden="true"><path d="M1.5 3.5h13v1L8 8.8 1.5 4.5zm0 2.3L8 10l6.5-4.2v6.7h-13z"/></svg>
          info@marlstonehouses.example.au
        </li>
      </ul>
      <p class="contact__post">PO Box 3817 Malaga WA 6944<br>17C Quenby Parade, Malaga WA 6090</p>
    </div>
  </section>

  <section class="card card--back" aria-label="Business card back">
    <div class="spot-uv-tree" role="img" aria-label="Spot UV gloss illustration of a wide leafy tree spreading across the card"></div>
    <div class="wordmark">MARLSTONE<br>BUILDWORKS</div>
  </section>
</main>
</body>
</html>
```